Need CATCHY/VIVID Banner design for my new UTV/ATV/Off Road Vehicle turn signal/lighting company

I need a banner ad designed so I can advertise on several different ATV (all terrain vehicle), UTV (Utility Vehicles), Golf Cart and Off-Road Vehicle forums. Ads need to be very catchy and produce a call to action. Action is getting hits to my website. Our main business is selling turn signal kits to make your side by side or your ATV/UTV street legal, as some states now allow you to drive these on public roads if you have the following items: Turn Signals, Horn, Lighted license plate bracket, headlights and brake lights. We sell all of these items for just about any model vehicle out there. Our call to action for this banner would be to get more website visits.

Target Market(s)

Off-road/outdoor enthusiasts,

Industry/Entity Type

Car Accessorie

Font styles to use
Sans Serif

Requirements
Must have
• Ad size need to be either 728x90 or 300x250. Colorful ad with an off-road vehicle integrated to the design (think UTV, side-by-side, etc.
Nice to have
• Nice to haves would be anything that makes this banner ad stand out on very boring web pages.
Should not have
• anything dull

```html
<!DOCTYPE html>
<html lang="en">
<head>
<meta charset="utf-8">
<title>Street Legal Banner Ads</title>
<link href="https://fonts.googleapis.com/css2?family=Alfa+Slab+One&family=Zilla+Slab:wght@700&family=Montserrat:wght@800&display=swap" rel="stylesheet">
<style>
  :root {
    --page: #ffffff;
    --red: #f20d0d;
    --ink: #111111;
    --orange: #ff9a00;
    --yellow: #ffd200;
    --white: #ffffff;
  }
  * { box-sizing: border-box; margin: 0; padding: 0; }
  html, body { width: 1200px; height: 874px; overflow: hidden; background: var(--page); }
  .banner {
    position: absolute;
    overflow: hidden;
    background: linear-gradient(160deg, var(--orange) 0%, #ffb400 45%, var(--yellow) 100%);
    font-family: "Zilla Slab", Georgia, serif;
    color: var(--ink);
  }
  .banner > * { position: absolute; }
  .banner--box { left: 374px; top: 154px; width: 450px; height: 375px; }
  .banner--leader { left: 53px; top: 585px; width: 1092px; height: 135px; }

  .vehicle-photo {
    border-radius: 40% 40% 18% 18%;
    background: radial-gradient(ellipse at 50% 55%, #5b4a44 0%, #7d3a2a 45%, rgba(230,90,30,.5) 75%, rgba(255,160,0,0) 100%);
  }
  .headline-word {
    font-family: "Alfa Slab One", Georgia, serif;
    font-weight: 400;
    color: var(--red);
    white-space: nowrap;
    line-height: 1;
  }
  .intro { font-weight: 700; white-space: nowrap; line-height: 1; }
  .kits-title { font-weight: 700; white-space: nowrap; line-height: 1; letter-spacing: .3px; transform-origin: left top; }
  .feature-list { list-style: none; transform-origin: left top; }
  .feature-list li { display: flex; align-items: center; white-space: nowrap; font-weight: 700; line-height: 1; }
  .tick { flex: none; }
  .brand {
    display: flex; align-items: center; gap: 6px;
    background: var(--ink);
    color: var(--white);
    font-family: "Montserrat", Arial, sans-serif;
    font-weight: 800;
    white-space: nowrap;
    border-radius: 3px;
  }
  .brand-mark { width: 12px; height: 12px; background: var(--red); flex: none; }
  .cta {
    display: flex; align-items: center; justify-content: center; gap: 6px;
    background: var(--red);
    color: var(--white);
    font-family: "Montserrat", Arial, sans-serif;
    font-weight: 800;
    border-radius: 999px;
    text-decoration: none;
    white-space: nowrap;
  }

  /* 300x250-style box */
  .banner--box .intro { left: 0; width: 450px; top: 14px; text-align: center; font-size: 28px; transform: scaleX(.95); }
  .banner--box .vehicle-photo { left: 5px; top: 124px; width: 326px; height: 210px; }
  .banner--box .street { left: 128px; top: 45px; font-size: 80px; transform: scaleX(.86); transform-origin: left top; }
  .banner--box .legal { right: 18px; top: 117px; font-size: 80px; transform: scaleX(.86); transform-origin: right top; }
  .banner--box .kits-title { left: 277px; top: 190px; font-size: 19px; transform: scaleX(.83); }
  .banner--box .feature-list { left: 277px; top: 206px; transform: scaleX(.85); }
  .banner--box .feature-list li { font-size: 13.5px; gap: 4px; height: 15.5px; }
  .banner--box .brand { left: 8px; top: 330px; width: 180px; height: 30px; padding: 0 8px; font-size: 9.5px; }
  .banner--box .cta { left: 245px; top: 321px; width: 179px; height: 31px; font-size: 15px; }

  /* 728x90-style leaderboard */
  .banner--leader .vehicle-photo { left: 44px; top: 4px; width: 212px; height: 140px; }
  .banner--leader .brand { left: 10px; top: 50px; width: 165px; height: 28px; padding: 0 7px; font-size: 8.5px; }
  .banner--leader .intro { right: 661px; font-size: 33px; text-align: right; transform: scaleX(.85); transform-origin: right center; }
  .banner--leader .intro-1 { top: 16px; }
  .banner--leader .intro-2 { top: 53px; }
  .banner--leader .intro-3 { top: 89px; }
  .banner--leader .street { left: 448px; top: 17px; font-size: 56px; transform: scaleX(.9); transform-origin: left top; }
  .banner--leader .legal { left: 448px; top: 72px; font-size: 56px; transform: scaleX(.9); transform-origin: left top; }
  .banner--leader .vehicle-photo--work { left: 658px; top: 9px; width: 166px; height: 130px; }
  .banner--leader .cta { left: 674px; top: 83px; width: 134px; height: 21px; font-size: 11px; }
  .banner--leader .kits-title { left: 821px; top: 22px; font-size: 27px; }
  .banner--leader .feature-list { left: 821px; top: 48px; }
  .banner--leader .feature-list li { font-size: 17.5px; gap: 5px; height: 23px; }
</style>
</head>
<body>

<svg width="0" height="0" style="position:absolute">
  <symbol id="tick" viewBox="0 0 20 20">
    <circle cx="10" cy="10" r="10" fill="#f20d0d"/>
    <path d="M5.5 10.5l3 3 6-7" fill="none" stroke="#fff" stroke-width="2.6" stroke-linecap="round" stroke-linejoin="round"/>
  </symbol>
  <symbol id="chevron" viewBox="0 0 10 16">
    <path d="M2 2l6 6-6 6" fill="none" stroke="#fff" stroke-width="2.8" stroke-linecap="round" stroke-linejoin="round"/>
  </symbol>
</svg>

<section class="banner banner--box">
  <p class="intro">Make your side by side or ATV/UTV</p>
  <div class="vehicle-photo" role="img" aria-label="Photo of a grey and red sport side-by-side with roll cage"></div>
  <h2 class="headline-word street">STREET</h2>
  <h2 class="headline-word legal">LEGAL</h2>
  <h3 class="kits-title">TURN SIGNAL KITS</h3>
  <ul class="feature-list">
    <li><svg class="tick" width="12" height="12"><use href="#tick"/></svg>Turn Signals, Horn,</li>
    <li><svg class="tick" width="12" height="12"><use href="#tick"/></svg>Lighted license plate bracket,</li>
    <li><svg class="tick" width="12" height="12"><use href="#tick"/></svg>Headlights and Brake lights</li>
  </ul>
  <div class="brand"><span class="brand-mark"></span>ROADWISE SIGNAL KITS</div>
  <a class="cta" href="#">VIEW PRODUCTS <svg width="9" height="14"><use href="#chevron"/></svg></a>
</section>

<section class="banner banner--leader">
  <div class="vehicle-photo" role="img" aria-label="Photo of a grey and red sport side-by-side with roll cage"></div>
  <div class="brand"><span class="brand-mark"></span>ROADWISE SIGNAL KITS</div>
  <p class="intro intro-1">Make your</p>
  <p class="intro intro-2">side by side</p>
  <p class="intro intro-3">or ATV/UTV</p>
  <h2 class="headline-word street">STREET</h2>
  <h2 class="headline-word legal">LEGAL</h2>
  <div class="vehicle-photo vehicle-photo--work" role="img" aria-label="Photo of a black utility vehicle with canopy roof"></div>
  <a class="cta" href="#">VIEW PRODUCTS <svg width="7" height="11"><use href="#chevron"/></svg></a>
  <h3 class="kits-title">TURN SIGNAL KITS</h3>
  <ul class="feature-list">
    <li><svg class="tick" width="16" height="16"><use href="#tick"/></svg>Turn Signals, Horn,</li>
    <li><svg class="tick" width="16" height="16"><use href="#tick"/></svg>Lighted license plate bracket,</li>
    <li><svg class="tick" width="16" height="16"><use href="#tick"/></svg>Headlights and Brake lights</li>
  </ul>
</section>

</body>
</html>
```